Payment Processor Website Design

Our company LumaPort, an online processor of payments is seeking talented submissions for our website redesign. The winning design will be chopped up and converted into a WordPress theme to allow for easy content additions and updates.

We are looking for modern designs that rival current websites in our industry (qindle.example, ploverbank.example, zunmo.example, kelvory.example, mossfieldcharges.example, harrowlinecharges.example, TuxCoin.example).

Our company is seeking to expand our reach to software developers and engineers who are either integrating our payment platform into their offerings or are engineering a custom solution for the company they work for and are in need of a payment platform such as our own.

We currently work with hundreds of different business partners whom either resell our services or integrate our processing capabilities into their software (which they sell). We also must communicate effectively to end users, businesses, who seek us out directly for their payment processing needs.

We are open to different color schemes but would ultimately like them to be somewhat inline with our current logo (see attached). Our website needs to instill security and confidence to any current and/or potential user as we are trusted with private and sensitive information.

We are seeking submissions from qualified; individual freelancers, freelance teams, and agencies who can attack this project in its entirety. Since this project is a total redesign, we would like submissions that have the capability to design any custom graphics, icons, buttons, and illustrations in line with our industry, capabilities, offerings, and content. We are looking for someone to design our new website and would prefer a vendor who can also help us to design elements (graphics, illustrations, charts, workflows) within our website.

Designs will be converted into a wordpress theme and we would like to utilize widgets for as many areas as possible to make editing and updating easy.

We are seeking the creation of a few unique pages but many of the pages for the majority of our content will just be internal content pages which will be duplicated.

We will likely contract with the winning submission for future work.

Please see Design Reference Document for more information

Target Market(s)

Resellers
Merchant Service Providers
Software Developers
Independent Sales Organizations (ISOs)
App Builders
Mobile App Builders
Independent Software Developers
Organizational Software Developers
Businesses who need to accept payments
Governments
Municipalities
Schools
DMVs
Courts
Retailers
Medical Offices
Hosipitals
Clinics
Dr. Offices
Gyms
Churches
Non-Profits
Software Companies
Technology Companies
Startups

Industry/Entity Type

Industry

Requirements
Should not have
• Logo cannot change drastically.

```html
<!DOCTYPE html>
<html lang="en">
<head>
<meta charset="utf-8">
<title>LumaPort – Payment Processing for the 21st Century</title>
<link rel="stylesheet" href="https://fonts.googleapis.com/css2?family=Open+Sans:wght@400;600;700&family=Montserrat:wght@400;600&display=swap">
<style>
  :root {
    --page-bg: #e9e9e9;
    --sheet: #ffffff;
    --topbar: #efefef;
    --ink: #1c1c1c;
    --text: #333333;
    --muted: #6b6b6b;
    --nav: #a3a3a3;
    --brand-blue: #3b8fcf;
    --brand-navy: #1f2f8c;
    --button-top: #4da6e6;
    --button-bottom: #2677b8;
    --card: #e8e8e8;
    --rule: #dcdcdc;
    --footer: #e6e6e6;
    --footer-box: #d9d9d9;
    --share: #3d6aa8;
  }
  * { box-sizing: border-box; margin: 0; padding: 0; }
  html, body { width: 1200px; height: 1088px; overflow: hidden; }
  body { background: var(--page-bg); font-family: "Open Sans", Arial, sans-serif; color: var(--text); }
  .sheet { position: absolute; left: 131px; top: 0; width: 938px; height: 1088px; background: var(--sheet); box-shadow: 0 0 8px rgba(0,0,0,.12); }

  .topbar { position: absolute; left: 0; top: 0; width: 938px; height: 30px; background: var(--topbar); }
  .search { position: absolute; left: 507px; top: 4px; width: 179px; height: 22px; background: #fff; border: 1px solid #c8c8c8; border-radius: 3px; font-size: 12px; color: #555; padding: 3px 6px; }
  .search svg { position: absolute; right: 6px; top: 4px; }
  .callus { position: absolute; left: 705px; top: 8px; font-size: 11.5px; color: #777; letter-spacing: .2px; }
  .callus strong { color: #333; font-weight: 600; }
  .contact-link { position: absolute; left: 860px; top: 8px; font-size: 11.5px; font-weight: 600; color: #333; }

  .header { position: absolute; left: 10px; top: 30px; width: 918px; height: 70px; border-bottom: 1px solid var(--rule); }
  .brand { position: absolute; left: 18px; top: 20px; display: flex; align-items: center; gap: 6px; font-family: "Open Sans", sans-serif; font-weight: 700; font-size: 24px; color: var(--brand-navy); }
  .brand-dot { width: 12px; height: 12px; background: #d8202a; border-radius: 50%; }
  .nav { position: absolute; left: 269px; top: 27px; display: flex; gap: 24px; font-size: 12.5px; font-weight: 600; letter-spacing: .3px; color: var(--nav); }
  .nav .active { color: var(--ink); }
  .login { position: absolute; left: 853px; top: 20px; width: 76px; height: 29px; border: 1px solid #bcd5ea; border-radius: 4px; color: var(--brand-blue); font-weight: 700; font-size: 14px; text-align: center; line-height: 27px; }
  .header .login { left: 843px; }

  .audience { position: absolute; top: 119px; width: 440px; height: 501px; background: var(--card); border-radius: 4px; overflow: hidden; }
  .audience--business { left: 19px; }
  .audience--developer { left: 479px; }
  .audience h2 { position: relative; z-index: 2; margin: 17px 20px 0; text-align: center; color: var(--brand-blue); font-size: 17px; font-weight: 700; line-height: 22px; }
  .audience p { position: relative; z-index: 2; margin: 16px 34px 0; text-align: center; font-size: 13.7px; line-height: 21.6px; color: var(--ink); }
  .audience p + p { margin-top: 22px; }
  .audience .photo { position: absolute; left: 0; right: 0; bottom: 0; height: 300px; z-index: 1; }
  .audience--business .photo { background: linear-gradient(180deg, rgba(232,232,232,1) 0%, rgba(215,218,222,.9) 25%, #b9bcc2 60%, #8e939b 100%); }
  .audience--developer .photo { background: linear-gradient(180deg, rgba(232,232,232,1) 0%, #d6d3cf 25%, #b7aea6 60%, #8f8a86 100%); }
  .cta { position: absolute; z-index: 3; top: 422px; left: 28px; width: 259px; height: 53px; border-radius: 4px; background: linear-gradient(180deg, var(--button-top), var(--button-bottom)); color: #fff; font-size: 17.5px; font-weight: 700; display: flex; align-items: center; box-shadow: 0 2px 3px rgba(0,0,0,.25); }
  .cta span { flex: 1; text-align: center; padding-right: 4px; }
  .cta i { width: 49px; height: 100%; border-left: 1px solid rgba(255,255,255,.35); display: flex; align-items: center; justify-content: center; }

  .intro { position: absolute; left: 0; top: 666px; width: 938px; text-align: center; }
  .intro h1 { font-family: "Montserrat", sans-serif; font-weight: 600; font-size: 37px; color: #111; letter-spacing: -.3px; }
  .intro .lead { margin-top: 4px; font-family: "Montserrat", sans-serif; font-size: 18.5px; color: var(--muted); }
  .intro-rule { position: absolute; left: 10px; top: 752px; width: 918px; height: 1px; background: var(--rule); }
  .about { position: absolute; left: 10px; top: 772px; width: 918px; text-align: center; font-size: 14px; line-height: 19px; color: #555; }
  .about p + p { margin-top: 12px; line-height: 24px; }

  .footer { position: absolute; left: 0; top: 908px; width: 938px; height: 129px; background: var(--footer); }
  .contact-box { position: absolute; left: 10px; top: 0; width: 216px; height: 129px; background: var(--footer-box); padding: 22px 19px; font-size: 13.5px; line-height: 16px; color: #444; }
  .contact-box h3 { font-size: 14px; font-weight: 700; color: #222; margin-bottom: 9px; letter-spacing: .3px; }
  .contact-box dl { display: grid; grid-template-columns: 54px auto; }
  .links { position: absolute; top: 26px; list-style: none; font-size: 14px; line-height: 26.4px; color: #555; }
  .links--a { left: 279px; }
  .links--b { left: 494px; }
  .share { position: absolute; left: 812px; top: 24px; }
  .share h4 { font-size: 14px; font-weight: 700; color: #222; margin-bottom: 4px; }
  .share ul { list-style: none; display: flex; gap: 6px; }
  .share li { width: 35px; height: 35px; background: var(--share); }

  .copyright { position: absolute; left: 0; top: 1057px; width: 938px; text-align: center; font-size: 12px; color: #444; letter-spacing: .2px; }
  .copyright span { margin: 0 8px; color: #888; }
</style>
</head>
<body>
<div class="sheet">
  <div class="topbar">
    <div class="search">Search
      <svg width="13" height="13" viewBox="0 0 13 13"><circle cx="5.3" cy="5.3" r="4" fill="none" stroke="#111" stroke-width="1.8"/><line x1="8.2" y1="8.2" x2="12" y2="12" stroke="#111" stroke-width="2"/></svg>
    </div>
    <div class="callus">CALL US ON: <strong>555 013 0199</strong></div>
    <div class="contact-link">CONTACT</div>
  </div>

  <header class="header">
    <div class="brand"><span class="brand-dot"></span>LumaPort</div>
    <nav class="nav">
      <span class="active">HOME</span><span>SOLUTIONS</span><span>PARTNERS</span><span>RESOURCES</span><span>DEVELOPERS</span><span>COMPANY</span><span>BLOG</span>
    </nav>
    <div class="login">LOGIN</div>
  </header>

  <section class="audience audience--business">
    <h2>Merchants, Businesses,<br>I have a business, Online Payment Processing, SaaS</h2>
    <p>This interactive graphic box will convey to the website visitor that this is where you click if you are a business and need to get setup to accept payments for your business with us.</p>
    <p>Something along the lines of maybe some skyscrapers, maybe a business disctrict</p>
    <div class="photo" role="img" aria-label="Photo of a smiling business team in suits seated at a meeting table"></div>
    <a class="cta"><span>Businesses Click Here</span><i><svg width="14" height="22" viewBox="0 0 14 22"><polyline points="2,2 11,11 2,20" fill="none" stroke="#fff" stroke-width="2.5"/></svg></i></a>
  </section>

  <section class="audience audience--developer">
    <h2>Developers, I Develop Software, Software Application Developers, Payment Processing API</h2>
    <p>Software Developers, Start-ups. Users who are looking to integrate a payment platform into their; website, ERP, CMS, mobile solution, software offering, some type of advanced integration requiring a custom integration with a payment processing platform, PaaS.</p>
    <p>Something graphically that speaks to software engineers and developers. Initial thoughts were maybe some gears moving with source code or programming languages incorporated.</p>
    <div class="photo" role="img" aria-label="Photo of a smiling developer in shirt and tie working at a laptop"></div>
    <a class="cta"><span>Devs Click Here</span><i><svg width="14" height="22" viewBox="0 0 14 22"><polyline points="2,2 11,11 2,20" fill="none" stroke="#fff" stroke-width="2.5"/></svg></i></a>
  </section>

  <section class="intro">
    <h1>Payment Processing for the 21st Century.</h1>
    <p class="lead">LumaPort provides the software, technology, and platform for multi-channel payment acceptance.</p>
  </section>
  <div class="intro-rule"></div>
  <section class="about">
    <p>Since 1992 we have been helping merchants streamline their payment acceptance. Whether your acceptance needs are online, at the poin-of-sale, or mobile; LumaPort can help.</p>
    <p>We provide both “out-of -the-box ” and custom solutions for your company or organization to begin taking paymentsin line with your needs and desires.</p>
  </section>

  <footer class="footer">
    <div class="contact-box">
      <h3>CONTACT INFORMATION</h3>
      <dl>
        <dt style="grid-column: 1 / 3">Lorem Ipsum. Proin gravida</dt>
        <dt>Phone:</dt><dd>555 013 0199</dd>
        <dt>Email:</dt><dd>info@lumaport.example</dd>
      </dl>
    </div>
    <ul class="links links--a"><li>ACH Processing</li><li>eCheck Processing</li><li>Paper Check Processing</li></ul>
    <ul class="links links--b"><li>ACH Processing</li><li>eCheck Processing</li><li>Paper Check Processing</li></ul>
    <div class="share">
      <h4>SHARE</h4>
      <ul><li aria-label="Share"></li><li aria-label="Share"></li><li aria-label="Share"></li></ul>
    </div>
  </footer>

  <div class="copyright">Copyright © 2014 LumaPort. All Rights Reserved<span>|</span>Privacy Policy<span>|</span>Terms of Use</div>
</div>
</body>
</html>
```